RW Hollis LLC Business Card - Civil Engineering & Consulting Firm

We need a Business Card that is elegant, and masculine.  It is our Professional Civil Engineering & Consulting Company located in San Antonio TX (Not s construction or builder firm- no gears & no tool images please). We provide civil engineering services including  commercial site plans, grading and drainage plans, utility plans, hydraulics and hydrology, land planning, utility coordination, and other general civil engineering services related to commercial and residential development.
We have 2 existing Logos. We would like to convey reliability, strength, trustworthiness and attention to detail.  Blues and orange tones as per logo We are OK with the use of a darker blue in the mix.  We have 2 logo versions - Full Company Name Logo to go on the back of card, & Small Icon Logo for the front w/ personal Info.

Target Market(s)
Architects, Real Estate Developers, Other Strctural Engineers, Surveyers, General Contractors
Industry/Entity Type
Professional Civil Engineering
Contact Information for Business Card
Name, Position, Address, Cell & Office #, email, and company website
Font styles to use
Other font styles liked:
- Avian
Requirements
Should not have
- No Tools, No Gears, no Cranes, or Construction Equipment.

```html
<!DOCTYPE html>
<html lang="en">
<head>
<meta charset="utf-8">
<title>RW Hollis LLC – Business Card</title>
<link rel="stylesheet" href="https://fonts.googleapis.com/css2?family=Jost:wght@400;500;600;700&display=swap">
<style>
  :root {
    --backdrop: #d6d7d9;
    --navy: #0f2146;
    --navy-deep: #0b1a3a;
    --sky: #6ea6dc;
    --orange: #f0901e;
    --white: #f4f6fa;
  }
  * { box-sizing: border-box; margin: 0; padding: 0; }
  html, body { width: 1200px; height: 800px; overflow: hidden; }
  body {
    background: var(--backdrop);
    font-family: "Jost", "Futura", sans-serif;
    position: relative;
  }
  .card {
    position: absolute;
    top: 252px;
    width: 525px;
    height: 300px;
    background: linear-gradient(135deg, var(--navy) 0%, var(--navy-deep) 100%);
    border-bottom: 3px solid var(--orange);
    box-shadow: 0 10px 24px rgba(0,0,0,0.22);
  }
  .card--front { left: 50px; }
  .card--back { left: 625px; }

  .card__frame {
    position: absolute;
    inset: 12px;
    border: 3px solid var(--sky);
  }
  .card--back .card__frame {
    inset: 16px;
    border-color: var(--orange);
  }

  /* front */
  .person {
    position: absolute;
    left: 48px;
    top: 122px;
    width: 200px;
    text-align: right;
  }
  .person__name {
    color: var(--orange);
    font-weight: 700;
    font-size: 24px;
    letter-spacing: 0.5px;
    line-height: 1;
  }
  .person__role {
    color: var(--sky);
    font-size: 16px;
    margin-top: 4px;
  }
  .divider {
    position: absolute;
    left: 266px;
    top: 100px;
    width: 1px;
    height: 100px;
    background: var(--sky);
    opacity: 0.7;
  }
  .contact {
    position: absolute;
    left: 284px;
    top: 96px;
    list-style: none;
    color: var(--white);
    font-size: 12.5px;
    line-height: 17px;
  }
  .contact__item { display: flex; align-items: flex-start; gap: 8px; }
  .contact__icon { width: 11px; height: 11px; margin-top: 3px; flex: none; }
  .contact__icon--blank { visibility: hidden; }
  .brand-mini {
    position: absolute;
    right: 32px;
    top: 30px;
    color: var(--sky);
    font-weight: 600;
    font-size: 13px;
    letter-spacing: 2px;
  }

  /* back */
  .brand {
    position: absolute;
    left: 0; right: 0;
    top: 112px;
    text-align: center;
  }
  .brand__name {
    color: var(--sky);
    font-weight: 500;
    font-size: 42px;
    letter-spacing: 5px;
    line-height: 1;
  }
  .brand__tagline {
    color: var(--orange);
    font-size: 12px;
    letter-spacing: 6px;
    margin-top: 14px;
  }
</style>
</head>
<body>
  <section class="card card--front" aria-label="Business card front">
    <div class="card__frame"></div>
    <div class="brand-mini">RW HOLLIS</div>
    <div class="person">
      <p class="person__name">DANIEL REYES</p>
      <p class="person__role">President</p>
    </div>
    <div class="divider"></div>
    <ul class="contact">
      <li class="contact__item">
        <svg class="contact__icon" viewBox="0 0 12 12"><path d="M6 0.5a4 4 0 0 0-4 4c0 3 4 7 4 7s4-4 4-7a4 4 0 0 0-4-4zm0 5.5a1.6 1.6 0 1 1 0-3.2 1.6 1.6 0 0 1 0 3.2z" fill="#f0901e"/></svg>
        <span>4120 Cedar Ridge Drive</span>
      </li>
      <li class="contact__item">
        <svg class="contact__icon contact__icon--blank" viewBox="0 0 12 12"></svg>
        <span>San Antonio, Texas 78209</span>
      </li>
      <li class="contact__item">
        <svg class="contact__icon" viewBox="0 0 12 12"><path d="M2.5 1l2 .2 1 2.6-1.3 1a6 6 0 0 0 3 3l1-1.3 2.6 1 .2 2c-5.5.6-9.1-3-8.5-8.5z" fill="#f0901e"/></svg>
        <span>210-555-0148</span>
      </li>
      <li class="contact__item">
        <svg class="contact__icon" viewBox="0 0 12 12"><rect x="3" y="0.8" width="6" height="10.4" rx="1" fill="none" stroke="#f0901e" stroke-width="1.4"/></svg>
        <span>210-555-0173</span>
      </li>
      <li class="contact__item">
        <svg class="contact__icon" viewBox="0 0 12 12"><rect x="0.5" y="2.5" width="11" height="7.5" fill="#f0901e"/><path d="M0.8 2.8L6 7l5.2-4.2" fill="none" stroke="#0f2146" stroke-width="1"/></svg>
        <span>reyes@rwhollis.com</span>
      </li>
      <li class="contact__item">
        <svg class="contact__icon" viewBox="0 0 12 12"><circle cx="6" cy="6" r="5.3" fill="#f0901e"/><path d="M0.8 6h10.4M6 0.8c-2.4 2.8-2.4 7.6 0 10.4M6 0.8c2.4 2.8 2.4 7.6 0 10.4" fill="none" stroke="#0f2146" stroke-width="0.9"/></svg>
        <span>www.rwhollis.com</span>
      </li>
    </ul>
  </section>

  <section class="card card--back" aria-label="Business card back">
    <div class="card__frame"></div>
    <div class="brand">
      <p class="brand__name">RW HOLLIS LLC</p>
      <p class="brand__tagline">CONSULTING ENGINEERS</p>
    </div>
  </section>
</body>
</html>
```